Half page Ad

I need to refresh my 1/2 page magazine ad. I will attach the current ad.

Industry/Entity Type

Financial Services

Colors
0054AA
0677BA
7BADD7
CADEEF
E8F1F8

```html
<!DOCTYPE html>
<html lang="en">
<head>
<meta charset="utf-8">
<title>Summit Ridge Financial Services – Half Page Ad</title>
<link rel="stylesheet" href="https://fonts.googleapis.com/css2?family=Tinos:ital,wght@0,400;0,700;1,700&family=Poppins:wght@400;500;600;700&display=swap">
<style>
  :root{
    --page:#c9c9c9;
    --navy:#22315a;
    --navy-deep:#141d33;
    --ink:#0c111d;
    --mint:#4fbf98;
    --white:#ffffff;
    --text-dark:#13203a;
  }
  *{margin:0;padding:0;box-sizing:border-box}
  html,body{width:1200px;height:830px;overflow:hidden;background:var(--page)}
  .ad{
    position:absolute;left:10px;top:33px;width:1180px;height:764px;overflow:hidden;
    background:linear-gradient(110deg,var(--navy) 0%,#1d2a4a 45%,var(--navy-deep) 75%,var(--ink) 100%);
    font-family:"Poppins",sans-serif;color:var(--white);
  }
  .ad__backdrop{position:absolute;inset:0}
  .brand{position:absolute;left:130px;top:54px;display:flex;align-items:center;gap:16px}
  .brand__mark{width:22px;height:22px;background:var(--white)}
  .brand__name{font-family:"Tinos",serif;font-weight:400;font-size:27px;letter-spacing:2px;line-height:1;color:var(--white)}
  .brand__sub{font-family:"Tinos",serif;font-size:14px;letter-spacing:4.5px;margin-top:4px;color:var(--white)}
  .headline{
    position:absolute;left:0;width:668px;top:150px;text-align:center;
    font-family:"Tinos",serif;font-style:italic;font-weight:700;font-size:72px;line-height:77px;
  }
  .banner{
    position:absolute;left:62px;top:313px;width:545px;height:44px;background:var(--mint);
    color:var(--text-dark);font-weight:500;font-size:31px;line-height:44px;text-align:center;
  }
  .services{position:absolute;top:390px;list-style:none;font-size:18px;line-height:31px}
  .services--left{left:68px}
  .services--right{left:424px;line-height:33px}
  .services li{display:flex;align-items:center;gap:10px}
  .services svg{width:22px;height:18px;flex:none}
  .partner{position:absolute;left:175px;top:508px;width:352px;text-align:center}
  .partner__name{font-weight:600;font-size:24px;line-height:28px;color:var(--mint)}
  .partner__tag{font-weight:500;font-size:13px;line-height:18px;letter-spacing:1.5px;color:var(--white);text-transform:uppercase}
  .call{position:absolute;left:61px;top:573px;font-family:"Tinos",serif;font-weight:700;font-size:66px;line-height:76px;white-space:nowrap}
  .call__label{color:var(--mint)}
  .footer-band{position:absolute;left:0;top:655px;width:650px;height:109px}
  .web{position:absolute;left:62px;top:668px;font-weight:600;font-size:36px;line-height:46px;color:var(--text-dark)}
  .address{position:absolute;left:62px;top:715px;font-weight:500;font-size:20.5px;line-height:26px;color:var(--text-dark)}
  .portrait{
    position:absolute;left:672px;top:129px;width:453px;height:506px;border:3px solid var(--mint);border-radius:20px;overflow:hidden;
    background:radial-gradient(ellipse at 60% 35%,#3c8f8a 0%,#245a6b 40%,#1a2f4e 75%,#111a2c 100%);
  }
  .portrait__name{
    position:absolute;left:0;right:0;bottom:0;height:90px;padding-top:16px;text-align:center;
    background:linear-gradient(to bottom,rgba(12,17,29,0) 0%,rgba(12,17,29,.92) 45%);
    font-family:"Tinos",serif;font-weight:700;font-size:44px;line-height:50px;letter-spacing:.5px;
  }
  .terms{position:absolute;right:61px;top:660px;font-style:italic;font-size:11px;color:var(--mint)}
  .fine{position:absolute;right:61px;top:682px;width:470px;text-align:right;font-style:italic;font-size:10.5px;line-height:14px;color:#e6e9ef}
</style>
</head>
<body>
<main class="ad">
  <svg class="ad__backdrop" viewBox="0 0 1180 764" preserveAspectRatio="none" aria-hidden="true">
    <defs>
      <linearGradient id="edgeGlow" x1="0" y1="0" x2="1" y2="0">
        <stop offset="0" stop-color="#0c111d" stop-opacity="0"/>
        <stop offset="1" stop-color="#4fbf98"/>
      </linearGradient>
      <linearGradient id="lowerGlow" x1="0" y1="0" x2="1" y2="1">
        <stop offset="0" stop-color="#0c111d" stop-opacity="0"/>
        <stop offset="1" stop-color="#2f8f6f" stop-opacity=".7"/>
      </linearGradient>
    </defs>
    <polygon points="577,0 1112,0 1040,190 780,120" fill="#0a0f1a" opacity=".85"/>
    <polygon points="960,0 1112,0 1020,200" fill="url(#edgeGlow)" opacity=".75"/>
    <polygon points="1180,460 1180,764 1000,764" fill="url(#lowerGlow)"/>
  </svg>

  <header class="brand">
    <span class="brand__mark"></span>
    <div>
      <div class="brand__name">SUMMIT RIDGE</div>
      <div class="brand__sub">FINANCIAL SERVICES</div>
    </div>
  </header>

  <h1 class="headline">Building On A<br>Firm Foundation</h1>
  <div class="banner">Navigating Volatile Markets</div>

  <ul class="services services--left">
    <li><svg viewBox="0 0 22 18"><path d="M2 9l6 6L20 2" fill="none" stroke="#4fbf98" stroke-width="3.5"/></svg>Financial Planning*</li>
    <li><svg viewBox="0 0 22 18"><path d="M2 9l6 6L20 2" fill="none" stroke="#4fbf98" stroke-width="3.5"/></svg>Estate Planning*</li>
    <li><svg viewBox="0 0 22 18"><path d="M2 9l6 6L20 2" fill="none" stroke="#4fbf98" stroke-width="3.5"/></svg>Effective Investment Strategies*</li>
  </ul>
  <ul class="services services--right">
    <li><svg viewBox="0 0 22 18"><path d="M2 9l6 6L20 2" fill="none" stroke="#4fbf98" stroke-width="3.5"/></svg>IRAs*</li>
    <li><svg viewBox="0 0 22 18"><path d="M2 9l6 6L20 2" fill="none" stroke="#4fbf98" stroke-width="3.5"/></svg>401k Rollovers*</li>
    <li><svg viewBox="0 0 22 18"><path d="M2 9l6 6L20 2" fill="none" stroke="#4fbf98" stroke-width="3.5"/></svg>Retirement Income*</li>
  </ul>

  <div class="partner">
    <p class="partner__name">Harbor Advisor Network</p>
    <p class="partner__tag">Member Advisor Program</p>
  </div>

  <p class="call"><span class="call__label">Call</span> : 555-014-2290</p>

  <svg class="footer-band" viewBox="0 0 650 109" preserveAspectRatio="none" aria-hidden="true">
    <polygon points="0,0 650,0 573,109 0,109" fill="#4fbf98"/>
  </svg>
  <p class="web">www.SummitRidgeFin.com</p>
  <p class="address">2200 Oak Lane , Suite 210, Cedar Falls, Tx 75001</p>

  <figure class="portrait" role="img" aria-label="Portrait photo of advisor Daniel Mercer in a navy blazer">
    <figcaption class="portrait__name">DANIEL MERCER</figcaption>
  </figure>

  <p class="terms">Terms &amp; Conditions</p>
  <p class="fine">Lorem ipsum dolor sit amet, consectetuer adipiscing elit, sed diam nonummy nibh euismod tincidunt ut laoreet dolore magna aliquam erat volutpat. Ut wisi enim ad minim veniam, quis nostrud exerci tation ullamcorper suscipit lobortis nisl ut aliquip ex ea</p>
</main>
</body>
</html>
```